landing page and 3 simple pages with descriptions of products

Landing page with company name. Create 3 unique pictures to link to three different pages on this this same domain.. See word document for details on the 4 pages required, the graphics/icons that need to be created. The six graphics should also be supplied for use on other marketing material.

Target Market(s)

our customer base: major laboratories across north america.

Coding

Coded - Design and coding required

Number of Pages Required

4 page

Requirements
Must have
• three images on the main page to link to the services we provide.
Nice to have
• Common theme across the title page, and the three sub pages.
• Page titles in the HTML that make sense to the items on the page.
Should not have
• scripts. sound.

```html
<!DOCTYPE html>
<html lang="en">
<head>
<meta charset="utf-8">
<title>Marlowe Services Inc. – Laboratory Services, Forge, Fabrication and More</title>
<link rel="stylesheet" href="https://fonts.googleapis.com/css2?family=Jost:wght@400;600&family=Didact+Gothic&display=swap">
<style>
  :root {
    --accent: #2b9fd8;
    --ink: #3a3a3a;
    --muted: #8a8a8a;
    --line: #e4e4e4;
    --footer-bg: #f8f8f8;
    --salmon: #f47f7d;
    --blue: #4b8fd5;
    --green: #86c06b;
    --purple: #b57dbc;
    --pink: #ff80c8;
    --orange: #f98e3a;
    --social-1: #2360b0;
    --social-2: #3ca9e0;
    --social-3: #1b6e9c;
    --social-4: #d8232a;
    --social-5: #f0a020;
  }
  * { box-sizing: border-box; margin: 0; padding: 0; }
  html, body { width: 1111px; height: 1200px; overflow: hidden; background: #fff; }
  body { position: relative; font-family: "Didact Gothic", sans-serif; color: var(--ink); border-top: 2px solid var(--accent); }

  .site-header { position: absolute; top: 0; left: 0; width: 1111px; height: 85px; }
  .brand { position: absolute; left: 90px; top: 30px; font-family: "Jost", sans-serif; font-size: 27px; font-weight: 400; letter-spacing: 0.3px; color: var(--ink); }
  .brand strong { font-weight: 600; }
  .menu { position: absolute; right: 90px; top: 28px; display: flex; align-items: center; gap: 6px; font-size: 11px; color: var(--ink); }
  .menu-button { width: 33px; height: 33px; border: 1.5px solid var(--accent); border-radius: 50%; display: flex; align-items: center; justify-content: center; }

  .hero { position: absolute; top: 85px; left: 0; width: 1111px; height: 404px; background: #f7f7f7; }
  .hero-photo { position: absolute; left: 0; top: 0; width: 700px; height: 404px;
    background: linear-gradient(90deg, #c9cccf 0%, #e2e4e6 40%, #eeeff0 72%, rgba(247,247,247,0) 100%); }
  .hero-title { position: absolute; left: 636px; top: 112px; font-family: "Jost", sans-serif; font-size: 28px; font-weight: 400; letter-spacing: 0.4px; color: var(--ink); }
  .hero-title strong { font-weight: 600; }
  .hero-text { position: absolute; left: 636px; top: 158px; width: 390px; font-size: 12px; line-height: 25.5px; color: var(--ink); }
  .hero-button { position: absolute; left: 636px; top: 257px; width: 153px; height: 33px; border: 1.5px solid var(--accent); border-radius: 2px; color: var(--accent); font-size: 12.5px; display: flex; align-items: center; justify-content: center; text-decoration: none; }
  .slider-dots { position: absolute; left: 943px; top: 330px; display: flex; gap: 19px; }
  .slider-dots span { width: 13px; height: 13px; border: 1px solid #999; border-radius: 50%; display: block; }
  .slider-dots .active { border-color: var(--accent); background: radial-gradient(circle, var(--accent) 0 3px, transparent 3.5px); }

  .services-title { position: absolute; top: 556px; left: 0; width: 1111px; text-align: center; font-family: "Jost", sans-serif; font-size: 28px; font-weight: 400; letter-spacing: 0.4px; }
  .services-title strong { font-weight: 600; }

  .service { position: absolute; width: 290px; text-align: center; text-decoration: none; color: var(--ink); }
  .service-badge { width: 99px; height: 99px; margin: 0 auto; border-radius: 50%; border: 1px solid var(--c); display: flex; align-items: center; justify-content: center; }
  .service-badge span { width: 91px; height: 91px; border-radius: 50%; background: var(--c); display: block; }
  .service-name { margin-top: 16px; font-size: 14px; }
  .service-text { margin-top: 6px; font-size: 11px; line-height: 20px; color: var(--muted); }

  .divider-v { position: absolute; width: 1px; background: var(--line); }
  .divider-h { position: absolute; height: 1px; background: var(--line); top: 844px; }

  .site-footer { position: absolute; top: 1109px; left: 0; width: 1111px; height: 91px; background: var(--footer-bg); }
  .copyright { position: absolute; left: 90px; top: 37px; font-size: 11px; color: var(--ink); }
  .social { position: absolute; right: 92px; top: 33px; display: flex; align-items: center; gap: 6px; font-size: 11px; }
  .social-label { margin-right: 6px; }
  .social a { width: 25px; height: 25px; border-radius: 50%; display: block; }
</style>
</head>
<body>
  <header class="site-header">
    <div class="brand"><strong>MARLOWE</strong> SERVICES INC.</div>
    <nav class="menu">MENU :
      <span class="menu-button">
        <svg width="17" height="13" viewBox="0 0 17 13"><g stroke="#2b9fd8" stroke-width="1.3"><line x1="0" y1="1" x2="17" y2="1"/><line x1="0" y1="6.5" x2="17" y2="6.5"/><line x1="0" y1="12" x2="17" y2="12"/></g></svg>
      </span>
    </nav>
  </header>

  <section class="hero">
    <div class="hero-photo" role="img" aria-label="Bright laboratory interior with an analyser, desks and cabinets"></div>
    <h1 class="hero-title">WELCOME TO <strong>MARLOWE</strong></h1>
    <p class="hero-text">Nemo enim ipsam voluptatem quia voluptas sit aspernatur aut odit aut fugit, sed quia consequuntur magni dolores eos qui rationerd voluptat sequi nesciunt. Neque porro quisquam...</p>
    <a class="hero-button" href="#">Learn More Information</a>
    <div class="slider-dots"><span class="active"></span><span></span><span></span></div>
  </section>

  <h2 class="services-title">OUR <strong>SERVICES</strong></h2>

  <a class="service" href="#" style="left:77px;top:627px;--c:var(--salmon)">
    <div class="service-badge"><span role="img" aria-label="Microscope icon"></span></div>
    <div class="service-name">National Laboratory Services</div>
    <div class="service-text">Nemo enim ipsam voluptatem quia voluptas aspernatur aut fugit, sed quia consequuntur...</div>
  </a>
  <a class="service" href="#" style="left:409px;top:627px;--c:var(--blue)">
    <div class="service-badge"><span role="img" aria-label="Anvil icon"></span></div>
    <div class="service-name">Marlowe Forge</div>
    <div class="service-text">Nemo enim ipsam voluptatem quia voluptas aspernatur aut fugit, sed quia consequuntur...</div>
  </a>
  <a class="service" href="#" style="left:741px;top:627px;--c:var(--green)">
    <div class="service-badge"><span role="img" aria-label="Bent metal strip icon"></span></div>
    <div class="service-name">Marlowe Fabrication</div>
    <div class="service-text">Nemo enim ipsam voluptatem quia voluptas aspernatur aut fugit, sed quia consequuntur...</div>
  </a>

  <a class="service" href="#" style="left:77px;top:873px;--c:var(--purple)">
    <div class="service-badge"><span role="img" aria-label="Fish icon"></span></div>
    <div class="service-name">Marlowe Farms</div>
    <div class="service-text">Nemo enim ipsam voluptatem quia voluptas aspernatur aut fugit, sed quia consequuntur...</div>
  </a>
  <a class="service" href="#" style="left:409px;top:873px;--c:var(--pink)">
    <div class="service-badge"><span role="img" aria-label="Rainbow and cloud icon"></span></div>
    <div class="service-name">Surplus Laboratory Equipment</div>
    <div class="service-text">Nemo enim ipsam voluptatem quia voluptas aspernatur aut fugit, sed quia consequuntur...</div>
  </a>
  <a class="service" href="#" style="left:741px;top:873px;--c:var(--orange)">
    <div class="service-badge"><span role="img" aria-label="Wedding rings icon"></span></div>
    <div class="service-name">Marriage Commissioner</div>
    <div class="service-text">Nemo enim ipsam voluptatem quia voluptas aspernatur aut fugit, sed quia consequuntur...</div>
  </a>

  <div class="divider-v" style="left:390px;top:628px;height:167px"></div>
  <div class="divider-v" style="left:724px;top:628px;height:167px"></div>
  <div class="divider-v" style="left:390px;top:876px;height:167px"></div>
  <div class="divider-v" style="left:724px;top:876px;height:167px"></div>
  <div class="divider-h" style="left:90px;width:274px"></div>
  <div class="divider-h" style="left:418px;width:275px"></div>
  <div class="divider-h" style="left:743px;width:276px"></div>

  <footer class="site-footer">
    <div class="copyright">Copyrights © . 2016 | Allrights Reserved.</div>
    <div class="social">
      <span class="social-label">Follow Our Social Networks :</span>
      <a href="#" aria-label="Social network 1" style="background:var(--social-1)"></a>
      <a href="#" aria-label="Social network 2" style="background:var(--social-2)"></a>
      <a href="#" aria-label="Social network 3" style="background:var(--social-3)"></a>
      <a href="#" aria-label="Social network 4" style="background:var(--social-4)"></a>
      <a href="#" aria-label="News feed" style="background:var(--social-5)"></a>
    </div>
  </footer>
</body>
</html>
```